Pediatric Dentist Business Card

I need a business card designed for a dentist who works exclusively with children.
We prefer designs that are out of ordiary that is fun and interesting to kids.

there is no logo since this is a dentists office. The name of the doctor is "Tavro Kine" if you want to get creative with that.

Target Market(s)

Kids

Industry/Entity Type

Business

Contact Information for Business Card

Anythings that is creative

Colors

Designer to choose colors to be used in the design.

```html
<!DOCTYPE html>
<html lang="en">
<head>
<meta charset="utf-8">
<title>Pediatric Dentist Business Card</title>
<link rel="stylesheet" href="https://fonts.googleapis.com/css2?family=Montserrat:wght@400;700&display=swap">
<style>
  :root {
    --green: #00a651;
    --card: #ffffff;
    --ink: #111111;
    --backdrop: #e9e9e7;
    --photo-light: #eef1ea;
    --photo-mid: #e8c9ad;
    --photo-warm: #d9a77c;
  }
  * { margin: 0; padding: 0; box-sizing: border-box; }
  html, body {
    width: 1200px;
    height: 1135px;
    overflow: hidden;
    background: var(--backdrop);
    font-family: "Montserrat", Arial, sans-serif;
    color: var(--ink);
  }
  .canvas { position: relative; width: 1200px; height: 1135px; }
  .card {
    position: absolute;
    left: 235px;
    width: 679px;
    height: 408px;
    background: var(--card);
    overflow: hidden;
    box-shadow: 0 6px 18px rgba(0,0,0,0.18);
  }
  .card-front { top: 90px; }
  .card-back { top: 621px; }

  .identity { position: absolute; left: 31px; top: 29px; }
  .identity .name { font-size: 27px; font-weight: 700; line-height: 1.1; }
  .identity .title { font-size: 12px; font-weight: 400; margin-top: 2px; }

  .contact {
    position: absolute;
    left: 31px;
    top: 276px;
    list-style: none;
    font-size: 14px;
    line-height: 21px;
  }

  .practice-name {
    position: absolute;
    color: var(--green);
    font-weight: 700;
    white-space: nowrap;
    transform: translate(-50%, -50%);
  }
  .card-front .practice-name { left: 521px; top: 203px; font-size: 22px; }
  .card-back .practice-name { left: 198px; top: 209px; font-size: 32px; }

  .base-band {
    position: absolute; left: 0; bottom: 0;
    width: 100%; height: 30px; background: var(--green);
  }
  .side-band {
    position: absolute; left: 0; top: 0;
    width: 31px; height: 100%; background: var(--green);
  }
  .photo-window { position: absolute; left: 0; top: 0; width: 679px; height: 408px; }
</style>
</head>
<body>
<div class="canvas">

  <section class="card card-front">
    <div class="identity">
      <h1 class="name">Tavro Kine</h1>
      <p class="title">Pediatric Dentist</p>
    </div>
    <p class="practice-name">Brightbay</p>
    <ul class="contact">
      <li>555 014 2783</li>
      <li>hi@brightbay.test</li>
      <li>www.brightbay.test</li>
      <li>12 Molar Lane</li>
    </ul>
    <div class="base-band"></div>
  </section>

  <section class="card card-back">
    <div class="side-band"></div>
    <p class="practice-name">Brightbay</p>
    <svg class="photo-window" viewBox="0 0 679 408">
      <defs>
        <linearGradient id="photo-tone" x1="0" y1="0" x2="0.6" y2="1">
          <stop offset="0" stop-color="var(--photo-light)"/>
          <stop offset="0.55" stop-color="var(--photo-mid)"/>
          <stop offset="1" stop-color="var(--photo-warm)"/>
        </linearGradient>
      </defs>
      <circle cx="565" cy="205" r="225" fill="none" stroke="var(--green)" stroke-width="10"/>
      <circle cx="565" cy="205" r="219" fill="url(#photo-tone)" role="img" aria-label="Photo of a smiling young girl brushing her teeth with a toothbrush"/>
    </svg>
  </section>

</div>
</body>
</html>
```